Summit Pilates Journeys Postcard Design

We need a promotional CMYK postcard that we will leave at yoga studios to advertise our yoga holidays to Cambodia.

Filecrate link with possible photos + logos (please see photo notes below): https://www.filecrate-share.net/sh/k4pq81mzx20vw5a/BBWnpLoq7Tz3HxKeRdaYbUmiQ?dl=0

Please message me if you need more info or have issues with the photos.

Thanks

Target Market(s)

Brand style:
High quality and discerning, healthy and ethically aware, natural, unique and boutique, a sense of exploration, pitched at busy professionals and high end consumers. (not hippy!)

Industry/Entity Type

Travel

Font styles to use
Serif
Sans Serif

Colors
abd036
0492cd

Requirements
Must have
• CMYK
• *I have attached a file crate link to various named pictures that you may use for your design selection but you are free to supply other royalty free pictures if you wish. There are a number of choices and we do not expect all of these to be used - just offering a selection so hopefully some will be suitable for your design. Here is the filecrate link: https://www.filecrate-share.net/sh/k4pq81mzx20vw5a/BBWnpLoq7Tz3HxKeRdaYbUmiQ?dl=0
• *Main front Picture must be one associated with Cambodia. Expecting several smaller photos on front as well
• *Must have at least one of our yoga photos on it.
• *The reverse side must have some white space around the address area so people could write a few lines and send as a postcard.
• *Please use the logo colours (lime and turquoise) with black or white as the main theme/colours.
• *Thinking to have a main photo of Cambodia on front with smaller photos and the 7 words featured (see text below).
• Text to include
• Front of postcard:
• (SPJ logo - prefer the coloured logo but needs to look ok with rest of photo - so can have white or black background or I have it in black & white - have attached coloured but message me if you wish for all B&W logo)
• Summit Pilates Journeys
• Explore, don't retreat!
• 7 night Grand Pilates Getaway Bundle.
• Siem Reap, Cambodia
• Discover
• Relax
• Cuisine
• Culture
• Yoga
• Boutique
• Ethical travel
• Reverse of postcard:
• Boutique, Unique, Fantastique!
• Do you need a high quality cultural holiday that explores, experiences, delights, relaxes, indulges - and has daily yoga? Are you short of time to do your holiday planning but still want some choices. Do you prefer a holiday over a strict yoga retreat? Do you want to use an ethical travel company to ensure your vacation does some good for others as well?
• Then visit:
• summitpilatesjourneys.com
• for dates and details.
• (also needs a box that I can stamp different codes into - must have white background - stamp text height is 4mm and max width is 27mm - needs the following text in or around the box)
• Special Promotion Code:
• Use this code with booking to receive a $200 AUD Tavrenko ecard
Nice to have
• Printers Specification (please see Printoria.com.au for other specifications if needed)
• Acceptable File Formats:
• We support a variety of file formats for uploaded designs.
• Adobe Acrobat 9 Document (*.pdf) (recommended)
• JPEG Image (*.jpg,*.jpeg)
• A6 postcard size:
• Full Bleed Size
• 151 x 108 mm
• 1783 x 1275 pixels
• Document Trim Size
• 148 x 105 mm
• 1748 x 1240 pixels
• CMYK
• Digital Imaging
• You may create printed products on our web site using digitized images from a variety of sources. Your designs, photos and images can come from a digital camera, scanner, or the Web.
• Any image you plan to use must be saved at approximately 300-dpi at 100% output size for the very best printing results. It’s helpful to know that shrinking an image on a product will increase its resolution. For example, an image captured at 600 x 900 pixels has 150-dpi at 4” x 6”. Howver, it can be printed at 300-dpi by reducing its dimensions on the product to 2” x 3”.
• Images from a Digital Camera
• If you wish to use images from a digital camera, before you snap pictures make sure the camera is set at a high enough resolution to result in 300 DPI at the intended photo print size. Most cameras have various settings for resolutions. The highest resolution for your camera depends on how many megapixels it has.
• You cannot increase the resolution of a photo after it is taken, except by reducing its printed dimensions (after you upload the image). Be careful when cropping a photo after it is taken. Cropping will reduce the number of pixels in the final image.
• Images from a Scanner
• Like a digital camera, a scanner must be preset to the proper resolution before image capture. Many scanners default to 150-dpi (or spi). Set your scanner’s resolution so that it results in 300-dpi at the image’s final print size. If your resulting scanned image is smaller than the recommended size or has less dpi than you need, you should either rescan your original at a higher resolution, or use the image for a smaller printed area.
• Images from the Web
• Images found on the web are typically at a resolution of 72-dpi. This resolution is much too low for quality printing. In addition, most images on the web are protected by copyright laws. For these reasons, we do not recommend using images from the web.
Should not have
• Hippy elements

```html
<!DOCTYPE html>
<html lang="en">
<head>
<meta charset="utf-8">
<title>Summit Pilates Journeys – Postcard Reverse</title>
<link href="https://fonts.googleapis.com/css2?family=Noto+Serif:ital,wght@1,700&family=Open+Sans:ital,wght@0,400;0,700;1,700&display=swap" rel="stylesheet">
<style>
  :root {
    --lime: #abd036;
    --turquoise: #1a92d0;
    --ink: #1a1a1a;
    --rule-grey: #c8c8c8;
    --frame-grey: #b0b0b0;
    --paper: #ffffff;
  }
  * { margin: 0; padding: 0; box-sizing: border-box; }
  html, body { width: 1200px; height: 858px; overflow: hidden; background: var(--paper); }
  .postcard {
    position: relative;
    width: 1200px;
    height: 858px;
    background: var(--paper);
    font-family: "Open Sans", Arial, sans-serif;
    color: var(--ink);
  }

  /* Headline block */
  .headline-rule {
    position: absolute;
    left: 15px;
    width: 646px;
    height: 2px;
    background: var(--lime);
  }
  .headline-rule--top { top: 34px; }
  .headline-rule--bottom { top: 93px; }
  .headline {
    position: absolute;
    left: 15px;
    width: 646px;
    top: 42px;
    text-align: center;
    font-family: "Noto Serif", Georgia, serif;
    font-style: italic;
    font-weight: 700;
    font-size: 34px;
    letter-spacing: 0.5px;
    color: var(--turquoise);
  }

  /* Questions */
  .questions { position: absolute; left: 31px; top: 119px; width: 610px; list-style: none; }
  .question {
    position: relative;
    padding-left: 38px;
    font-size: 17.2px;
    line-height: 24px;
    margin-bottom: 16px;
  }
  .question-marker {
    position: absolute;
    left: 2px;
    top: 3px;
    width: 20px;
    height: 20px;
  }

  /* Call to action */
  .brand-mark { position: absolute; left: 687px; top: 14px; }
  .brand-name {
    position: absolute;
    left: 687px;
    top: 110px;
    font-size: 17px;
    font-weight: 700;
    color: var(--lime);
    white-space: nowrap;
  }
  .cta-lead { position: absolute; left: 687px; top: 149px; font-size: 17px; }
  .cta-url { position: absolute; left: 686px; top: 166px; font-size: 22px; color: var(--turquoise); }
  .cta-tail { position: absolute; left: 687px; top: 196px; font-size: 17px; }

  .stamp-box {
    position: absolute;
    left: 1060px;
    top: 30px;
    width: 112px;
    height: 124px;
    border: 1px solid var(--frame-grey);
  }

  /* Promotion */
  .promo-label { position: absolute; left: 687px; top: 246px; font-size: 17px; font-weight: 700; }
  .promo-code-box {
    position: absolute;
    left: 900px;
    top: 240px;
    width: 216px;
    height: 33px;
    border: 1px solid #555;
    border-radius: 17px;
    background: var(--paper);
  }
  .promo-note {
    position: absolute;
    left: 687px;
    top: 281px;
    width: 430px;
    font-size: 17px;
    font-weight: 700;
    font-style: italic;
    line-height: 25px;
  }

  /* Address area */
  .address-box {
    position: absolute;
    left: 686px;
    top: 396px;
    width: 502px;
    height: 365px;
    border: 1px solid var(--frame-grey);
  }
  .address-line {
    position: absolute;
    left: 22px;
    right: 22px;
    height: 1px;
    background: var(--rule-grey);
  }

  .footer-band {
    position: absolute;
    left: 0;
    bottom: 0;
    width: 1200px;
    height: 24px;
    background: var(--turquoise);
  }
</style>
</head>
<body>
<main class="postcard">
  <div class="headline-rule headline-rule--top"></div>
  <h1 class="headline">Boutique, Unique, Fantastique!</h1>
  <div class="headline-rule headline-rule--bottom"></div>

  <ul class="questions">
    <li class="question">
      <svg class="question-marker" viewBox="0 0 20 20"><circle cx="10" cy="10" r="8" fill="none" stroke="var(--turquoise)" stroke-width="2.5"/></svg>
      Do you need a high quality cultural holiday that explores, experiences, delights, relaxes, indulges - and has daily yoga?
    </li>
    <li class="question">
      <svg class="question-marker" viewBox="0 0 20 20"><circle cx="10" cy="10" r="8" fill="none" stroke="var(--turquoise)" stroke-width="2.5"/></svg>
      Are you short of time to do your holiday planning but still want some choices. Do you prefer a holiday over a strict yoga retreat?
    </li>
    <li class="question">
      <svg class="question-marker" viewBox="0 0 20 20"><circle cx="10" cy="10" r="8" fill="none" stroke="var(--turquoise)" stroke-width="2.5"/></svg>
      Do you want to use an ethical travel company to ensure your vacation does some good for others as well?
    </li>
  </ul>

  <svg class="brand-mark" width="84" height="84" viewBox="0 0 84 84" aria-hidden="true">
    <circle cx="42" cy="42" r="38" fill="none" stroke="var(--turquoise)" stroke-width="5"/>
  </svg>
  <p class="brand-name">Summit Pilates Journeys</p>

  <p class="cta-lead">Then visit:</p>
  <p class="cta-url">www.summitpilatesjourneys.com</p>
  <p class="cta-tail">for dates and details.</p>

  <div class="stamp-box"></div>

  <p class="promo-label">Special Promotion Code:</p>
  <div class="promo-code-box"></div>
  <p class="promo-note">Use this code with booking to receive a $200 AUD Tavrenko ecard</p>

  <div class="address-box">
    <div class="address-line" style="top:91px"></div>
    <div class="address-line" style="top:161px"></div>
    <div class="address-line" style="top:231px"></div>
    <div class="address-line" style="top:302px"></div>
  </div>

  <div class="footer-band"></div>
</main>
</body>
</html>
```